Product Development BELM (The Pinecrest Leisure Collective)

We are a sporting goods company who engages in "Total product Development" from A - Z incorporating customer collaboration and input. We research, collaborate and design, build, and ship for the customer. We have a PPT page which describes this process, but it is BORING and lacks "Fun". Our industry is an OUTDOOR company - Camping, Hunting, Fishing, etc. This process needs to be an illustration of the process and emphasizing the company process with fun illustrations.

Industry/Entity Type

It Company

```html
<!DOCTYPE html>
<html lang="en">
<head>
<meta charset="utf-8">
<title>Total Product Development from A - Z</title>
<link href="https://fonts.googleapis.com/css2?family=Barlow:wght@400;500;600;700&display=swap" rel="stylesheet">
<style>
  :root {
    --orange: #c8762a;
    --grey-dark: #6d6e70;
    --grey-mid: #a7a9ac;
    --grey-light: #cfd0d2;
    --ink: #111111;
    --white: #ffffff;
  }
  * { margin: 0; padding: 0; box-sizing: border-box; }
  html, body { width: 1200px; height: 848px; overflow: hidden; background: var(--white); }
  .sheet { position: relative; width: 1200px; height: 848px; font-family: "Barlow", Arial, sans-serif; }
  .title-band {
    position: absolute; left: 0; top: 0; width: 1200px; height: 92px;
    background: var(--orange); color: var(--white);
    display: flex; align-items: center; justify-content: center;
    font-size: 52px; font-weight: 700; letter-spacing: 1.4px;
  }
  .process-map { position: absolute; left: 0; top: 0; }
  .step-label { font-family: "Barlow", Arial, sans-serif; font-weight: 600; font-size: 18px; fill: var(--ink); text-anchor: middle; letter-spacing: 0.3px; }
  .icon { fill: none; stroke: var(--grey-mid); stroke-width: 2; }
  .icon-solid { fill: var(--grey-mid); }
  .footer-band {
    position: absolute; left: 0; top: 737px; width: 1200px; height: 111px;
    background: var(--grey-dark);
  }
  .brand-name {
    position: absolute; left: 28px; top: 34px;
    display: flex; align-items: center; gap: 10px;
    color: var(--white); font-size: 34px; font-weight: 700; line-height: 40px;
  }
  .brand-dot { width: 14px; height: 14px; border-radius: 50%; background: var(--white); }
  .mission {
    position: absolute; left: 222px; top: 30px; width: 975px;
    color: var(--white); font-size: 17px; line-height: 22px; font-weight: 400;
  }
</style>
</head>
<body>
<div class="sheet">
  <header class="title-band">TOTAL PRODUCT DEVELOPMENT" FROM A - Z</header>

  <svg class="process-map" width="1200" height="737" viewBox="0 0 1200 737" aria-label="Process steps">
    <defs>
      <polygon id="hex-outer" points="-114,0 -64,-99 64,-99 114,0 64,99 -64,99"/>
      <polygon id="hex-inner" points="-94,0 -52,-81 52,-81 94,0 52,81 -52,81"/>
    </defs>

    <polygon class="flow-arrow" fill="var(--grey-dark)" points="22,126 130,126 130,98 225,152 130,207 130,178 22,178"/>
    <polygon class="flow-arrow" fill="var(--orange)" points="1172,645 1063,645 1063,612 970,667 1063,722 1063,690 1172,690"/>

    <g class="ring-grey" fill="var(--grey-light)">
      <use href="#hex-outer" x="428" y="315"/>
      <use href="#hex-outer" x="772" y="315"/>
      <use href="#hex-outer" x="428" y="512"/>
      <use href="#hex-outer" x="772" y="512"/>
    </g>
    <g class="ring-orange" fill="var(--orange)">
      <use href="#hex-outer" x="600" y="216"/>
      <use href="#hex-outer" x="258" y="413"/>
      <use href="#hex-outer" x="942" y="413"/>
      <use href="#hex-outer" x="600" y="611"/>
    </g>
    <use href="#hex-outer" x="600" y="413" fill="var(--grey-dark)"/>

    <g class="face" fill="var(--white)" stroke="#222" stroke-width="1.5">
      <use href="#hex-inner" x="600" y="216"/>
      <use href="#hex-inner" x="428" y="315"/>
      <use href="#hex-inner" x="772" y="315"/>
      <use href="#hex-inner" x="258" y="413"/>
      <use href="#hex-inner" x="600" y="413"/>
      <use href="#hex-inner" x="942" y="413"/>
      <use href="#hex-inner" x="428" y="512"/>
      <use href="#hex-inner" x="772" y="512"/>
      <use href="#hex-inner" x="600" y="611"/>
    </g>

    <g class="icon">
      <circle cx="598" cy="160" r="9"/><rect x="593" y="169" width="10" height="8"/>
      <path d="M598 142v-5 M584 148l-3-3 M612 148l3-3 M580 160h-4 M616 160h4"/>
      <rect x="411" y="246" width="32" height="22"/><path d="M415 263l8-8 6 4 10-10 M427 268l-6 10 M427 268l6 10"/>
      <circle cx="771" cy="264" r="17"/><path d="M754 264h34 M771 247c-8 10-8 24 0 34 M771 247c8 10 8 24 0 34"/>
      <circle cx="259" cy="349" r="6"/><path d="M259 346v3h3 M246 361h4l4 12h14l3-9h-18"/><circle cx="256" cy="377" r="2"/><circle cx="266" cy="377" r="2"/>
      <circle cx="937" cy="350" r="10"/><circle cx="952" cy="362" r="5"/><path d="M928 372h22 M937 360v12"/>
      <path d="M755 456l17-8 17 8z M757 459h30 M760 462v14 M767 462v14 M777 462v14 M784 462v14 M755 479h34"/>
      <circle cx="580" cy="556" r="10"/><path d="M587 563l10 10 M598 560l15-12 15 12v20h-30z"/>
    </g>
    <g class="icon-solid">
      <rect x="580" y="355" width="6" height="20"/><rect x="590" y="350" width="6" height="25"/>
      <path d="M578 383v-8h44v8z"/><path d="M600 375l8-8v8l8-8v8z"/>
      <circle cx="428" cy="452" r="6"/><path d="M420 462h16l2 16h-4v8h-12v-8h-4z"/>
    </g>

    <text class="step-label" x="600" y="209">CUSTOMER</text>
    <text class="step-label" x="600" y="233">COLLABORATION</text>
    <text class="step-label" x="428" y="308">DESIGN &amp;</text>
    <text class="step-label" x="428" y="332">DEVELOPMENT</text>
    <text class="step-label" x="772" y="308">GLOBAL</text>
    <text class="step-label" x="772" y="332">SOURCING</text>
    <text class="step-label" x="258" y="406">QUALITY</text>
    <text class="step-label" x="258" y="430">ASSURANCE</text>
    <text class="step-label" x="600" y="419">MANUFACTURING</text>
    <text class="step-label" x="942" y="407">PRODUCT</text>
    <text class="step-label" x="942" y="431">TESTING</text>
    <text class="step-label" x="428" y="506">CUSTOMER</text>
    <text class="step-label" x="428" y="530">SERVICE</text>
    <text class="step-label" x="772" y="506">FULFILLEMENT</text>
    <text class="step-label" x="772" y="530">&amp; DISTRIBUTION</text>
    <text class="step-label" x="600" y="605">WAREHOUSING</text>
    <text class="step-label" x="600" y="629">JIT INVENTORY</text>
  </svg>

  <footer class="footer-band">
    <div class="brand-name"><span class="brand-dot"></span>BELM</div>
    <p class="mission">The Pinecrest Leisure Collective is commited to being the leading price + value company providing quality and innovation to the<br>marketplace. Our customer is our number one priority, and our goal every day is to service our customers to the best of our ability.</p>
  </footer>
</div>
</body>
</html>
```